Fern Hollow Animal Hospital Postcard Design

I need a postcard for grand opening. The front of the card should have our business name and logo, below the logo I want to have a coupon for " Free office visit or $ 20 off of packages " for the first time clients.

I want to have the packages prices and details on the back of the postcard, the details of the packages are attached.

```html
<!DOCTYPE html>
<html lang="en">
<head>
<meta charset="utf-8">
<title>Fern Hollow Animal Hospital – Grand Opening Postcard</title>
<link href="https://fonts.googleapis.com/css2?family=Montserrat:wght@400;500;600;700;800&display=swap" rel="stylesheet">
<style>
  :root {
    --bg: #e9e9ea;
    --green-light: #9acd2a;
    --green: #7fb522;
    --green-dark: #5f9a18;
    --ink: #232323;
    --white: #ffffff;
    --orange-light: #fbb62a;
    --orange: #f48f16;
    --card-text: #3c3c3c;
    --box-top: #f4f4f4;
    --box-bottom: #e2e2e2;
  }
  * { margin: 0; padding: 0; box-sizing: border-box; }
  html, body { width: 1200px; height: 1200px; overflow: hidden; }
  body {
    background: var(--bg);
    font-family: 'Montserrat', Arial, sans-serif;
    position: relative;
  }
  .postcard {
    position: absolute;
    top: 195px;
    width: 470px;
    height: 811px;
    background: var(--white);
    overflow: hidden;
  }
  .postcard--front { left: 106px; }
  .postcard--back { left: 624px; }
  .postcard svg.shapes { position: absolute; inset: 0; }

  .brand-title {
    position: absolute;
    left: 0; right: 0;
    text-align: center;
    line-height: 1;
  }
  .brand-title__name {
    display: block;
    color: var(--white);
    font-weight: 700;
    font-size: 44px;
    letter-spacing: 0.5px;
  }
  .brand-title__sub {
    display: block;
    color: var(--ink);
    font-weight: 500;
    font-size: 32px;
    margin-top: 4px;
  }
  .postcard--front .brand-title { top: 56px; }
  .postcard--back .brand-title { top: 32px; }

  .brand-name {
    position: absolute;
    top: 168px; left: 0; right: 0;
    text-align: center;
    font-size: 58px;
    line-height: 70px;
    font-weight: 800;
    color: var(--ink);
    letter-spacing: -1px;
  }

  .coupon {
    position: absolute;
    left: 94px; top: 282px;
    width: 282px; height: 122px;
  }
  .coupon svg { position: absolute; inset: 0; }
  .coupon__headline {
    position: absolute; top: 16px; left: 0; right: 0;
    text-align: center; font-weight: 700; font-size: 21px; line-height: 26px; color: var(--ink);
  }
  .coupon__divider {
    position: absolute; top: 49px; left: 34px; right: 34px;
    border-top: 3px dotted #3a3a3a;
  }
  .coupon__offer {
    position: absolute; top: 58px; left: 0; right: 0;
    text-align: center; font-weight: 800; font-size: 36px; color: var(--white);
    line-height: 1;
  }
  .coupon__note {
    position: absolute; top: 98px; left: 0; right: 0;
    text-align: center; font-size: 10px; letter-spacing: 6px; color: var(--ink);
  }

  .photo { position: absolute; }
  .photo--front-pets {
    left: 60px; top: 430px; width: 370px; height: 360px;
    border-radius: 45% 45% 8% 8%;
    background: radial-gradient(ellipse at 45% 45%, #c98a45 0%, #b7793c 40%, rgba(160,130,95,0.6) 70%, rgba(220,220,220,0) 100%);
  }
  .photo--back-left {
    left: 14px; top: 590px; width: 240px; height: 200px;
    border-radius: 40% 40% 10% 10%;
    background: radial-gradient(ellipse at 40% 50%, #f2f2f2 0%, #b9b9bd 50%, rgba(150,150,155,0) 100%);
  }
  .photo--back-right {
    left: 316px; top: 604px; width: 136px; height: 94px;
    border-radius: 45% 45% 20% 20%;
    background: radial-gradient(ellipse at 50% 50%, #5a4a3a 0%, #8a6b48 45%, rgba(140,110,80,0) 100%);
  }

  .packages {
    position: absolute;
    left: 54px; top: 183px;
    width: 362px;
    display: grid;
    grid-template-columns: 174px 174px;
    column-gap: 14px;
    row-gap: 12px;
  }
  .package {
    height: 86px;
    border-radius: 10px;
    background: linear-gradient(160deg, var(--box-top) 0%, var(--box-bottom) 100%);
    box-shadow: 0 2px 4px rgba(0,0,0,0.18);
    padding: 14px 6px 0 6px;
  }
  .package__title {
    font-size: 8.4px; font-weight: 700; color: var(--green-dark);
    white-space: nowrap; margin-bottom: 4px;
  }
  .package__label { font-size: 8.5px; color: var(--card-text); margin-bottom: 4px; }
  .package__items { list-style: none; font-size: 6.6px; line-height: 1.35; color: var(--card-text); }

  .contact {
    position: absolute; left: 263px; top: 733px; color: var(--white);
  }
  .contact__label { font-weight: 700; font-size: 12px; }
  .contact__row { display: flex; align-items: center; gap: 6px; margin-top: 5px; }
  .contact__phone { font-weight: 700; font-size: 15px; }
  .contact__web { font-weight: 600; font-size: 8.5px; }
</style>
</head>
<body>

<section class="postcard postcard--front">
  <svg class="shapes" width="470" height="811" viewBox="0 0 470 811">
    <defs>
      <linearGradient id="frontGreen" x1="0" y1="0" x2="0" y2="1">
        <stop offset="0" stop-color="var(--green-light)"/>
        <stop offset="1" stop-color="var(--green)"/>
      </linearGradient>
      <linearGradient id="frontFloor" x1="0" y1="0" x2="0" y2="1">
        <stop offset="0" stop-color="#f1f1f1"/>
        <stop offset="1" stop-color="#d9d9d9"/>
      </linearGradient>
      <mask id="wordmarkGap">
        <rect x="0" y="0" width="470" height="811" fill="#fff"/>
        <rect x="58" y="170" width="354" height="72" fill="#000"/>
      </mask>
    </defs>
    <path d="M0 0 H470 V196 C400 196 360 200 300 212 C220 228 120 210 0 213 Z" fill="url(#frontGreen)"/>
    <g mask="url(#wordmarkGap)">
      <path d="M470 196 C400 196 360 200 300 212 C220 228 120 210 0 213" fill="none" stroke="var(--ink)" stroke-width="2"/>
      <path d="M470 202 C400 202 360 206 300 218 C220 234 120 216 0 219" fill="none" stroke="var(--ink)" stroke-width="1" stroke-dasharray="4 3"/>
    </g>
    <path d="M0 601 Q235 391 470 573 V811 H0 Z" fill="url(#frontFloor)"/>
    <path d="M0 601 Q235 391 470 573" fill="none" stroke="var(--ink)" stroke-width="9"/>
    <path d="M0 612 Q235 402 470 584" fill="none" stroke="var(--green-light)" stroke-width="5"/>
    <path d="M0 594 Q235 384 470 566" fill="none" stroke="var(--green-light)" stroke-width="1.2" stroke-dasharray="5 3"/>
    <path d="M0 620 Q235 410 470 592" fill="none" stroke="var(--green-light)" stroke-width="1.2" stroke-dasharray="5 3"/>
  </svg>

  <h1 class="brand-title">
    <span class="brand-title__name">FERN HOLLOW</span>
    <span class="brand-title__sub">ANIMAL HOSPITAL</span>
  </h1>

  <div class="brand-name">Fern Hollow</div>

  <div class="coupon">
    <svg width="282" height="122" viewBox="0 0 282 122">
      <defs>
        <linearGradient id="couponOrange" x1="0" y1="0" x2="0" y2="1">
          <stop offset="0" stop-color="var(--orange-light)"/>
          <stop offset="1" stop-color="var(--orange)"/>
        </linearGradient>
      </defs>
      <path d="M6 0 H276 A6 6 0 0 1 282 6 V47 A14 14 0 0 0 282 75 V116 A6 6 0 0 1 276 122 H6 A6 6 0 0 1 0 116 V75 A14 14 0 0 0 0 47 V6 A6 6 0 0 1 6 0 Z" fill="url(#couponOrange)"/>
    </svg>
    <div class="coupon__headline">FREE OFFICE VISIT</div>
    <div class="coupon__divider"></div>
    <div class="coupon__offer">$20 OFF</div>
    <div class="coupon__note">OF PACKAGES</div>
  </div>

  <div class="photo photo--front-pets" role="img" aria-label="Photo of a golden puppy sitting beside a tabby kitten"></div>
</section>

<section class="postcard postcard--back">
  <svg class="shapes" width="470" height="811" viewBox="0 0 470 811">
    <defs>
      <linearGradient id="backGreen" x1="0" y1="0" x2="0" y2="1">
        <stop offset="0" stop-color="var(--green-light)"/>
        <stop offset="1" stop-color="var(--green)"/>
      </linearGradient>
      <linearGradient id="backFooter" x1="0" y1="0" x2="1" y2="1">
        <stop offset="0" stop-color="var(--green-light)"/>
        <stop offset="1" stop-color="var(--green-dark)"/>
      </linearGradient>
    </defs>
    <path d="M0 0 H470 V118 C400 118 380 140 300 138 C200 135 100 120 0 136 Z" fill="url(#backGreen)"/>
    <path d="M470 118 C400 118 380 140 300 138 C200 135 100 120 0 136" fill="none" stroke="var(--ink)" stroke-width="2"/>
    <path d="M470 124 C400 124 380 146 300 144 C200 141 100 126 0 142" fill="none" stroke="var(--ink)" stroke-width="1" stroke-dasharray="4 3"/>
    <path d="M0 800 Q230 563 470 765 V811 H0 Z" fill="url(#backFooter)"/>
    <path d="M0 792 Q230 555 470 757" fill="none" stroke="var(--ink)" stroke-width="7"/>
    <path d="M0 806 Q230 569 470 771" fill="none" stroke="var(--white)" stroke-width="1.2" stroke-dasharray="5 3"/>
  </svg>

  <h2 class="brand-title">
    <span class="brand-title__name">FERN HOLLOW</span>
    <span class="brand-title__sub">ANIMAL HOSPITAL</span>
  </h2>

  <div class="packages">
    <article class="package">
      <h3 class="package__title">ANNUAL DOG PACKAGE$99</h3>
      <p class="package__label">INCLUDES</p>
      <ul class="package__items">
        <li>Complete physical exam DHLPP Vaccine Bor-</li>
        <li>detella vaccine Rabies Vaccine Fecal exam</li>
        <li>Heartworm test Deworming</li>
      </ul>
    </article>
    <article class="package">
      <h3 class="package__title">PUPPY PACKAGE-1 (7-10WEEK) $49</h3>
      <ul class="package__items">
        <li>Complete physical exam</li><li>DHLPP Vaccine</li><li>Bordettella vaccine</li><li>Fecal exam</li><li>Deworming</li>
      </ul>
    </article>
    <article class="package">
      <h3 class="package__title">PUPPY PACKAGE-2 (10-13WEEK) $49</h3>
      <ul class="package__items">
        <li>Complete physical exam</li><li>DHLPP Vaccine</li><li>Bordettella vaccine</li><li>Fecal exam</li><li>Deworming</li>
      </ul>
    </article>
    <article class="package">
      <h3 class="package__title">PUPPY PACKAGE-3 (13-16WEEK) $49</h3>
      <ul class="package__items">
        <li>Complete physical exam</li><li>DHLPP Vaccine</li><li>Bordettella vaccine</li><li>Fecal exam</li><li>Deworming</li>
      </ul>
    </article>
    <article class="package">
      <h3 class="package__title">ANNUAL CAT PACKAGE $69</h3>
      <ul class="package__items">
        <li>Complete physical exam</li><li>FvRcP Vaccine</li><li>Rabies Vaccine</li><li>Fecal exam</li><li>Deworming</li>
      </ul>
    </article>
    <article class="package">
      <h3 class="package__title">KITTEN PACKAGE-1 &nbsp;$ 49 (7-10 WEEK)</h3>
      <ul class="package__items">
        <li>Complete physical exam</li><li>FvRcP Vaccine</li><li>Fecal exam</li><li>Deworming</li>
      </ul>
    </article>
    <article class="package">
      <h3 class="package__title">KITTEN PACKAGE-2 &nbsp;$ 49 (10-13 WEEK)</h3>
      <ul class="package__items">
        <li>Complete physical exam</li><li>FvRcP Vaccine</li><li>Fecal exam</li><li>Deworming</li>
      </ul>
    </article>
    <article class="package">
      <h3 class="package__title">KITTEN PACKAGE-3 &nbsp;$ 49 (13-16 WEEK)</h3>
      <ul class="package__items">
        <li>Complete physical exam</li><li>FvRcP Vaccine</li><li>Rabies Vaccine</li><li>Fecal exam</li><li>Deworming</li>
      </ul>
    </article>
  </div>

  <div class="photo photo--back-left" role="img" aria-label="Photo of a white husky lying beside a grey cat"></div>
  <div class="photo photo--back-right" role="img" aria-label="Photo of a tabby cat and a black and white dog peeking over the curve"></div>

  <div class="contact">
    <div class="contact__label">CONTACT US:</div>
    <div class="contact__row">
      <svg width="14" height="14" viewBox="0 0 14 14" aria-hidden="true">
        <rect x="0" y="0" width="14" height="14" rx="2" fill="var(--white)"/>
        <path d="M4 3 L6 3 L6.6 5.2 L5.4 6 C6 7.4 6.8 8.2 8 8.8 L8.8 7.6 L11 8.2 L11 10 C7 10.4 3.6 7 4 3 Z" fill="var(--green-dark)"/>
      </svg>
      <span class="contact__phone">+1 555 0142 7788</span>
    </div>
    <div class="contact__row">
      <svg width="14" height="14" viewBox="0 0 14 14" aria-hidden="true" fill="none" stroke="var(--white)" stroke-width="1">
        <circle cx="7" cy="7" r="6"/>
        <ellipse cx="7" cy="7" rx="2.6" ry="6"/>
        <line x1="1" y1="7" x2="13" y2="7"/>
        <line x1="2" y1="4" x2="12" y2="4"/>
        <line x1="2" y1="10" x2="12" y2="10"/>
      </svg>
      <span class="contact__web">www.fernhollowvet.com</span>
    </div>
  </div>
</section>

</body>
</html>
```